Operating Model for KTR

Please convert the diagram on slide 3 to a professional design. Slides 1 and 2 gives a sense of the colour scheme - although not as bold as those - but sympathetic colours. But the KTR logo is to appear on the slide.
Further instructions in the slide

```html
<!DOCTYPE html>
<html lang="en">
<head>
<meta charset="utf-8">
<title>KTR Operating Model</title>
<link href="https://fonts.googleapis.com/css2?family=Open+Sans:wght@400;600;700;800&display=swap" rel="stylesheet">
<style>
  :root {
    --magenta: #c81d5e;
    --orange: #f0704f;
    --red: #e5202e;
    --deep-red: #a91d2a;
    --grey: #b9b9bd;
    --grey-text: #d9d9dc;
    --ink: #231f20;
    --white: #ffffff;
  }
  html, body {
    margin: 0;
    padding: 0;
    width: 1200px;
    height: 800px;
    overflow: hidden;
    background: var(--white);
    font-family: "Open Sans", Arial, sans-serif;
  }
  .operating-model { display: block; width: 1200px; height: 800px; }
  .tri { stroke-width: 22; stroke-linejoin: round; filter: url(#lift); }
  .tri--magenta { fill: var(--magenta); stroke: var(--magenta); }
  .tri--orange { fill: var(--orange); stroke: var(--orange); }
  .tri--red { fill: var(--red); stroke: var(--red); }
  .tri--deep { fill: var(--deep-red); stroke: var(--deep-red); }
  .tri-label { fill: var(--white); font-weight: 700; font-size: 11px; text-anchor: middle; }
  .tri-label--small { font-size: 9.5px; }
  .icon { fill: none; stroke: var(--ink); stroke-width: 2.2; stroke-linecap: round; stroke-linejoin: round; }
  .pillar-title { font-weight: 700; font-size: 22px; text-anchor: middle; }
  .pillar-title--planning { fill: var(--magenta); }
  .pillar-title--attracting { fill: var(--orange); }
  .pillar-title--building { fill: var(--red); }
  .sector-band { fill: var(--grey); }
  .sector-label { fill: var(--grey-text); font-size: 12px; font-weight: 600; text-anchor: middle; }
  .core-planning { fill: var(--orange); }
  .core-renewal { fill: var(--magenta); }
  .core-label { fill: var(--white); font-weight: 800; font-size: 24px; text-anchor: middle; }
  .flow { fill: none; stroke-width: 17; }
  .flow--orange { stroke: var(--orange); }
  .flow--magenta { stroke: var(--magenta); }
  .flow-label { fill: var(--white); font-size: 9px; font-weight: 700; text-anchor: middle; dominant-baseline: middle; }
  .brand-mark { fill: var(--red); }
  .brand-name { fill: var(--ink); font-weight: 600; font-size: 18px; }
</style>
</head>
<body>
<svg class="operating-model" viewBox="0 -50 1108 738" preserveAspectRatio="xMidYMid meet" xmlns="http://www.w3.org/2000/svg" role="img" aria-label="KTR operating model: Skills Planning and Skills Renewal cycle">
  <defs>
    <filter id="lift" x="-20%" y="-20%" width="140%" height="140%">
      <feDropShadow dx="2" dy="3" stdDeviation="3" flood-color="#000" flood-opacity="0.18"/>
    </filter>
    <marker id="head-orange" viewBox="0 0 10 10" refX="2" refY="5" markerWidth="2" markerHeight="2.2" orient="auto">
      <path d="M0 0 L10 5 L0 10 Z" fill="#f0704f"/>
    </marker>
    <marker id="head-magenta" viewBox="0 0 10 10" refX="2" refY="5" markerWidth="2" markerHeight="2.2" orient="auto">
      <path d="M0 0 L10 5 L0 10 Z" fill="#c81d5e"/>
    </marker>
    <path id="pillar-arc" d="M193 449 A385 385 0 0 1 963 449"/>
    <path id="sector-arc" d="M368 449 A205 205 0 0 1 778 449"/>
    <path id="lbl-community" d="M504 301.5 A138 138 0 0 1 585 283.5"/>
    <path id="lbl-government" d="M597 285.1 A138 138 0 0 1 661.7 315.3"/>
    <path id="lbl-future" d="M678.7 332.3 A138 138 0 0 1 710.5 433"/>
    <path id="lbl-productivity" d="M661.7 526.7 A138 138 0 0 0 710.5 433"/>
    <path id="lbl-quality" d="M561 558.4 A138 138 0 0 0 652.2 534"/>
    <path id="lbl-feedback" d="M467.3 509.7 A138 138 0 0 0 549 556.9"/>
    <path id="lbl-students" d="M437.1 397 A138 138 0 0 0 460 500.2"/>
    <path id="lbl-industry" d="M439.7 385.3 A138 138 0 0 1 493.8 308"/>
  </defs>

  <!-- Pillar titles -->
  <text class="pillar-title pillar-title--planning"><textPath href="#pillar-arc" startOffset="11%">Planning for Skilling</textPath></text>
  <text class="pillar-title pillar-title--attracting"><textPath href="#pillar-arc" startOffset="44%">Attracting Students</textPath></text>
  <text class="pillar-title pillar-title--building"><textPath href="#pillar-arc" startOffset="78%">Building Future Skills</textPath></text>

  <!-- Education sectors band -->
  <path class="sector-band" d="M328 449 A250 250 0 0 1 828 449 Z"/>
  <text class="sector-label"><textPath href="#sector-arc" startOffset="13%">Schooling</textPath></text>
  <text class="sector-label"><textPath href="#sector-arc" startOffset="33%">Community Education</textPath></text>
  <text class="sector-label"><textPath href="#sector-arc" startOffset="58%">Vocational Education</textPath></text>
  <text class="sector-label"><textPath href="#sector-arc" startOffset="83%">Higher Education</textPath></text>

  <!-- Function triangles -->
  <g class="function function--engagement">
    <polygon class="tri tri--magenta" points="240,338 240,466 360,407"/>
    <g class="icon" transform="translate(270,368)">
      <circle cx="0" cy="0" r="6"/><circle cx="-11" cy="-11" r="3.5"/><circle cx="11" cy="-11" r="3.5"/><circle cx="-11" cy="11" r="3.5"/><circle cx="11" cy="11" r="3.5"/>
      <path d="M-8 -8 L-4 -4 M8 -8 L4 -4 M-8 8 L-4 4 M8 8 L4 4"/>
    </g>
    <text class="tri-label" x="288" y="406">Engagement and</text>
    <text class="tri-label" x="288" y="419">Collaboration</text>
    <text class="tri-label" x="288" y="432">Front door</text>
  </g>

  <g class="function function--insights">
    <polygon class="tri tri--magenta" points="337,206 268,320 394,316"/>
    <text class="tri-label" x="330" y="246">Skills</text>
    <text class="tri-label" x="330" y="258">data and</text>
    <text class="tri-label" x="330" y="270">insights</text>
    <g class="icon" transform="translate(357,298)">
      <path d="M-15 0 Q0 -12 15 0 Q0 12 -15 0 Z"/><circle cx="0" cy="0" r="5"/>
    </g>
  </g>

  <g class="function function--provision">
    <polygon class="tri tri--orange" points="360,158 478,114 468,240"/>
    <text class="tri-label" x="428" y="157">Provision</text>
    <text class="tri-label" x="428" y="170">Planning KTR</text>
    <text class="tri-label" x="428" y="183">Skills Plan</text>
    <g class="icon" transform="translate(450,214)">
      <path d="M-8 -14 H5 L10 -9 V14 H-8 Z"/><path d="M-4 -6 H5 M-4 0 H5 M-4 6 H1"/><circle cx="8" cy="10" r="5"/><path d="M6 10 L8 12 L11 8"/>
    </g>
  </g>

  <g class="function function--acquisition">
    <polygon class="tri tri--orange" points="495,98 625,98 562,210"/>
    <text class="tri-label" x="560" y="120">Student</text>
    <text class="tri-label" x="560" y="133">Acquisition</text>
    <text class="tri-label" x="560" y="146">and Guidance</text>
    <g class="icon" transform="translate(562,177)">
      <path d="M-20 -4 L-10 -10 L0 -6 L10 -10 L20 -4"/><path d="M-14 0 L-4 10 Q0 13 4 9 L14 0"/><path d="M-6 -2 L2 6 M0 -4 L7 3"/>
    </g>
  </g>

  <g class="function function--feedback">
    <polygon class="tri tri--red" points="640,100 782,160 660,232"/>
    <text class="tri-label" x="698" y="152">Skills Feedback</text>
    <text class="tri-label" x="698" y="164">Employers and</text>
    <text class="tri-label" x="698" y="176">Students</text>
    <g class="icon" transform="translate(680,204)">
      <rect x="-14" y="-10" width="16" height="12" rx="3"/><path d="M-10 2 L-12 7 L-5 2"/><rect x="-2" y="-3" width="16" height="12" rx="3"/><path d="M10 9 L12 14 L5 9"/>
    </g>
  </g>

  <g class="function function--quality">
    <polygon class="tri tri--red" points="803,176 880,290 746,294"/>
    <text class="tri-label tri-label--small" x="806" y="214">Quality</text>
    <text class="tri-label tri-label--small" x="806" y="225">workforce</text>
    <text class="tri-label tri-label--small" x="806" y="236">course design</text>
    <text class="tri-label tri-label--small" x="806" y="247">recognition</text>
    <g class="icon" transform="translate(790,272)" style="stroke-width:3">
      <path d="M10 -8 A13 13 0 1 0 13 2"/><path d="M-6 -1 L0 6 L14 -12"/>
    </g>
  </g>

  <g class="function function--innovation">
    <polygon class="tri tri--deep" points="860,296 925,430 795,372"/>
    <text class="tri-label" x="865" y="345">Skills</text>
    <text class="tri-label" x="865" y="357">innovation</text>
    <g class="icon" transform="translate(842,380)">
      <circle cx="0" cy="0" r="8"/><circle cx="0" cy="0" r="3"/>
      <path d="M0 -12 V-8 M0 8 V12 M-12 0 H-8 M8 0 H12 M-8.5 -8.5 L-5.7 -5.7 M8.5 8.5 L5.7 5.7 M-8.5 8.5 L-5.7 5.7 M8.5 -8.5 L5.7 -5.7"/>
    </g>
  </g>

  <!-- Flow ring -->
  <g class="flow-ring">
    <path class="flow flow--magenta" marker-end="url(#head-magenta)" d="M710.5 433 A138 138 0 0 0 684 342"/>
    <path class="flow flow--magenta" marker-end="url(#head-magenta)" d="M661.7 526.7 A138 138 0 0 0 705 452"/>
    <path class="flow flow--magenta" marker-end="url(#head-magenta)" d="M561 558.4 A138 138 0 0 0 636 544"/>
    <path class="flow flow--magenta" marker-end="url(#head-magenta)" d="M467.3 509.7 A138 138 0 0 0 532 554"/>
    <path class="flow flow--orange" marker-end="url(#head-orange)" d="M437.1 397 A138 138 0 0 0 451 486"/>
    <path class="flow flow--orange" marker-end="url(#head-orange)" d="M493.8 308 A138 138 0 0 0 444 369"/>
    <path class="flow flow--orange" marker-end="url(#head-orange)" d="M585 283.5 A138 138 0 0 0 518 294"/>
    <path class="flow flow--orange" marker-end="url(#head-orange)" d="M661.7 315.3 A138 138 0 0 0 614 289"/>

    <text class="flow-label"><textPath href="#lbl-community" startOffset="50%">Community</textPath></text>
    <text class="flow-label"><textPath href="#lbl-government" startOffset="50%">Government</textPath></text>
    <text class="flow-label"><textPath href="#lbl-future" startOffset="55%">Future Skills</textPath></text>
    <text class="flow-label"><textPath href="#lbl-productivity" startOffset="50%">Productivity</textPath></text>
    <text class="flow-label"><textPath href="#lbl-quality" startOffset="45%">Quality</textPath></text>
    <text class="flow-label"><textPath href="#lbl-feedback" startOffset="45%">Feedback</textPath></text>
    <text class="flow-label"><textPath href="#lbl-students" startOffset="45%">Students</textPath></text>
    <text class="flow-label"><textPath href="#lbl-industry" startOffset="55%">Industry</textPath></text>
  </g>

  <!-- Core: Skills Planning / Skills Renewal -->
  <g class="core">
    <circle class="core-renewal" cx="573" cy="421" r="110"/>
    <path class="core-planning" d="M590 312 A110 110 0 0 0 515 514 C540 468 600 455 612 395 C620 358 608 328 590 312 Z"/>
    <text class="core-label" x="545" y="375">Skills</text>
    <text class="core-label" x="545" y="393">Planning</text>
    <text class="core-label" x="575" y="468">Skills</text>
    <text class="core-label" x="575" y="486">Renewal</text>
  </g>

  <!-- Brand -->
  <g class="brand">
    <circle class="brand-mark" cx="92" cy="563" r="22"/>
    <text class="brand-name" x="124" y="560">KTR Skills</text>
    <text class="brand-name" x="124" y="579">Council</text>
  </g>
</svg>
</body>
</html>
```